Australian residential property business needs a business card design

I need a business card design for my new business 'Harbour Estate Ventures'. The business will involve house purchases, land development sites, renovation projects, sub-divisions etc. I will be buying property from motivated vendors and working with property investors. I will deal with a wide range of people working in the residential property market including real estate agents, councils, tradespeople, banks, home owners, etc.

I would like something simple, not flashy, but a little bit unique. The colours should be in line with my logo. The business card needs to be professional. I would like something memorable, but not 'busy' or too bright. Not boring. Modern ok.

Target Market(s)

Home owners looking to sell their property, real estate agents, tradespeople (e.g. plumbers, builders, electricians etc), property investors, local councils, and anyone else involved in the residential property industry

Industry/Entity Type

Business

Contact Information for Business Card

I need to include my business name/logo, my name, my title, a PO Box number/address, a mobile number, and an email address.

Font styles to use
Serif

Requirements
Must have
• My business card details listed above.

```html
<!DOCTYPE html>
<html lang="en">
<head>
<meta charset="utf-8">
<title>Harbour Estate Ventures – Business Card</title>
<link rel="stylesheet" href="https://fonts.googleapis.com/css2?family=Lato:wght@400;700&display=swap">
<style>
  :root {
    --backdrop: #e9ebea;
    --paper: #ffffff;
    --green: #1e9410;
    --orange-deep: #f29000;
    --orange-mid: #f6b445;
    --orange-glow: #fff6d8;
    --brand: #e8960f;
    --ink: #2b2b2b;
  }
  * { margin: 0; padding: 0; box-sizing: border-box; }
  html, body {
    width: 1200px;
    height: 898px;
    overflow: hidden;
    background: var(--backdrop);
    font-family: "Lato", sans-serif;
    color: var(--ink);
  }
  .card {
    position: absolute;
    left: 139px;
    top: 170px;
    width: 935px;
    height: 553px;
    background: var(--paper);
    overflow: hidden;
  }
  .card-bands {
    position: absolute;
    inset: 0;
    width: 935px;
    height: 553px;
  }
  .brand {
    position: absolute;
    left: 0;
    right: 0;
    top: 150px;
    display: flex;
    align-items: center;
    justify-content: center;
    gap: 14px;
  }
  .brand-mark {
    width: 30px;
    height: 30px;
    background: var(--green);
  }
  .brand-name {
    font-size: 32px;
    font-weight: 700;
    color: var(--brand);
    letter-spacing: 0.5px;
  }
  .holder {
    position: absolute;
    left: 162px;
    top: 356px;
  }
  .holder-name {
    font-size: 25px;
    font-weight: 700;
    line-height: 1;
  }
  .holder-title {
    margin-top: 10px;
    font-size: 25px;
    font-weight: 400;
    letter-spacing: 5px;
    line-height: 1;
  }
  .contacts {
    position: absolute;
    left: 400px;
    top: 356px;
    list-style: none;
  }
  .contact {
    position: absolute;
    left: 0;
    display: flex;
    align-items: center;
    gap: 12px;
    font-size: 26px;
    white-space: nowrap;
    line-height: 1;
  }
  .contact-phone { top: 0; }
  .contact-email { top: 43px; }
  .contact-post { top: 118px; }
  .contact-icon {
    width: 28px;
    height: 28px;
    flex: none;
  }
</style>
</head>
<body>
  <div class="card">
    <svg class="card-bands" viewBox="0 0 935 553" aria-hidden="true">
      <defs>
        <radialGradient id="orangeGlow" cx="290" cy="402" r="700" gradientUnits="userSpaceOnUse">
          <stop offset="0" stop-color="var(--orange-glow)"/>
          <stop offset="0.35" stop-color="var(--orange-mid)"/>
          <stop offset="0.75" stop-color="var(--orange-deep)"/>
        </radialGradient>
      </defs>
      <path class="band-green" d="M0,285 H760 C840,285 900,250 935,180 V205 C905,265 850,298 760,298 H0 Z" fill="var(--green)"/>
      <path class="band-orange" d="M0,304 H770 C850,304 905,282 935,258 V553 H0 Z" fill="url(#orangeGlow)"/>
    </svg>

    <div class="brand">
      <span class="brand-mark"></span>
      <span class="brand-name">Harbour Estate Ventures</span>
    </div>

    <div class="holder">
      <p class="holder-name">Your Name</p>
      <p class="holder-title">Position</p>
    </div>

    <ul class="contacts">
      <li class="contact contact-phone">
        <svg class="contact-icon" viewBox="0 0 28 28" aria-hidden="true">
          <rect x="7" y="3" width="14" height="22" rx="2" fill="none" stroke="var(--ink)" stroke-width="2"/>
          <line x1="12" y1="21" x2="16" y2="21" stroke="var(--ink)" stroke-width="2"/>
        </svg>
        <span>123-456-7888</span>
      </li>
      <li class="contact contact-email">
        <svg class="contact-icon" viewBox="0 0 28 28" aria-hidden="true">
          <rect x="3" y="7" width="22" height="15" fill="none" stroke="var(--ink)" stroke-width="2"/>
          <path d="M3,7 L14,16 L25,7" fill="none" stroke="var(--ink)" stroke-width="2"/>
        </svg>
        <span>name@companyname.com</span>
      </li>
      <li class="contact contact-post">
        <svg class="contact-icon" viewBox="0 0 28 28" aria-hidden="true">
          <path d="M14,3 C9,3 6,7 6,11 C6,17 14,25 14,25 C14,25 22,17 22,11 C22,7 19,3 14,3 Z" fill="var(--ink)"/>
          <circle cx="14" cy="11" r="3" fill="var(--orange-mid)"/>
        </svg>
        <span>PO Box, Address</span>
      </li>
    </ul>
  </div>
</body>
</html>
```